Business Card Design Project

I need a business card design for our new logo, please check the logo at the following link:
https://www.filecrate.net/s/q7rtx2pw9kd41m/FernLoop.png
The address on the business card:
Av. Gervásio Tavares 418 sala 207
Barra da Tijuca, Rio de Janeiro, RJ
CEP: 22714-380
Brasil
Phone: +55 21 86347215
e-mail: osvaldo@fernloop.com.br
Updates
Thank you all for sending your designs, we will not provide feedback because there are too many designs, on December 3 we will pick the best design according to our point of view. Please keep posting.
Osvaldo
Industry/Entity Type
Business
Look and feel
Each slider illustrates characteristics of the customer's brand and the style your logo design should communicate.

```html
<!DOCTYPE html>
<html lang="en">
<head>
<meta charset="utf-8">
<title>FernLoop Business Card</title>
<link rel="stylesheet" href="https://fonts.googleapis.com/css2?family=Open+Sans:wght@400;600;700&display=swap">
<style>
  :root {
    --ink: #2a2a2a;
    --accent: #f2c12e;
    --card: #ffffff;
    --card-edge: #e9e9e9;
    --stage-top: #cfcfcf;
    --stage-bottom: #f4f4f4;
  }
  * { margin: 0; padding: 0; box-sizing: border-box; }
  html, body { width: 1200px; height: 1000px; overflow: hidden; }
  body {
    font-family: "Open Sans", Arial, sans-serif;
    color: var(--ink);
    background: linear-gradient(180deg, var(--stage-top) 0%, var(--stage-bottom) 70%, #ffffff 100%);
  }
  .stage {
    width: 1200px; height: 1000px;
    display: flex; justify-content: center; align-items: center; gap: 90px;
  }
  .card {
    width: 340px; height: 580px;
    background: linear-gradient(180deg, var(--card) 0%, #f3f3f3 100%);
    border-radius: 22px;
    border: 1px solid var(--card-edge);
    box-shadow: 0 14px 30px rgba(0,0,0,0.18);
    position: relative;
  }
  .brand {
    display: flex; align-items: center; gap: 12px;
    font-weight: 700; color: var(--ink);
  }
  .brand-dot {
    border-radius: 50%;
    background: var(--accent);
    flex: none;
  }
  /* front */
  .card-front { display: flex; justify-content: center; align-items: center; }
  .card-front .brand { font-size: 54px; letter-spacing: 1px; }
  .card-front .brand-dot { width: 38px; height: 38px; }
  /* back */
  .card-back { padding: 70px 0 0; text-align: center; }
  .card-back .brand { justify-content: center; font-size: 30px; }
  .card-back .brand-dot { width: 22px; height: 22px; }
  .holder { margin-top: 46px; }
  .holder-name { font-size: 27px; font-weight: 700; letter-spacing: 0.5px; }
  .holder-role { font-size: 15px; margin-top: 2px; }
  .contact { margin-top: 40px; font-size: 12.5px; line-height: 1.45; }
  .contact dt {
    color: var(--accent); font-weight: 700; font-size: 12.5px; margin-top: 8px;
  }
  .contact dd { color: var(--ink); }
</style>
</head>
<body>
<main class="stage">
  <section class="card card-front" aria-label="Card front">
    <div class="brand"><span class="brand-dot"></span><span class="brand-name">FernLoop</span></div>
  </section>

  <section class="card card-back" aria-label="Card back">
    <div class="brand"><span class="brand-dot"></span><span class="brand-name">FernLoop</span></div>
    <div class="holder">
      <p class="holder-name">Name Surname</p>
      <p class="holder-role">Position</p>
    </div>
    <dl class="contact">
      <dt>Address</dt>
      <dd>Av. Gervásio Tavares 418 sala 207<br>Barra da Tijuca, Rio de Janeiro, RJ Brasil</dd>
      <dt>Phone</dt>
      <dd>+55 21 86347215</dd>
      <dt>E-mail</dt>
      <dd>osvaldo@fernloop.com.br</dd>
    </dl>
  </section>
</main>
</body>
</html>
```